Photoshop Templates for Instagram, x 2

A Square template to reuse that is on brand.

It will involve an image and text of between 3 and 10 words.
I would like 2 separate contrasting images to use interchangeably

In the files I have added some of the images that I have been using, as well as the home page of my website that is currently being developed.

The on brand would be very recognisable with the website.

Requirements
Must have
• Must be similar in feel to the home page.

Must be simple to to change image and and text in the template

I would like 2 designs. Both similar, but contrasting

The square images show the look that I have been using (created by myself, so I'm sure these can be massively improved upon)

```html
<!DOCTYPE html>
<html lang="en">
<head>
<meta charset="utf-8">
<title>PEAKMIND – Instagram Post Templates</title>
<link rel="stylesheet" href="https://fonts.googleapis.com/css2?family=Jost:wght@500;700;800&display=swap">
<style>
  :root {
    --stage: #b4b4b4;
    --ink-white: #ffffff;
    --brand-grey: #c9c9c9;
    --night: #05070d;
    --stadium-blue: #2b4fb8;
    --sky-blue: #5f86e0;
    --deep-blue: #0b1a55;
    --accent-teal: #2fd0c4;
    --accent-blue: #1f3fe0;
    --pitch-green: #1f3a2a;
    --sock-green: #2aa680;
    --boot-lime: #b8c24a;
    --mist-teal: #3f7f8c;
    --stripe-sand: #e9d2b4;
  }
  * { box-sizing: border-box; margin: 0; padding: 0; }
  html, body {
    width: 1200px;
    height: 625px;
    overflow: hidden;
    background: var(--stage);
    font-family: "Jost", "Futura", sans-serif;
  }
  .template-row { position: relative; width: 1200px; height: 625px; }
  .post {
    position: absolute;
    top: 36px;
    width: 547px;
    height: 547px;
    overflow: hidden;
    background: var(--night);
  }
  .post--stadium { left: 30px; }
  .post--strike { left: 621px; }
  .post svg { display: block; width: 100%; height: 100%; }
  .headline-lead, .headline-main {
    font-family: "Jost", "Futura", sans-serif;
    fill: var(--ink-white);
  }
  .headline-lead { font-size: 80px; font-weight: 700; }
  .headline-main { font-size: 132px; font-weight: 800; }
  .brand-name {
    font-family: "Jost", "Futura", sans-serif;
    font-weight: 700;
    font-size: 34px;
    fill: var(--brand-grey);
  }
  .brand-tagline {
    font-family: "Jost", "Futura", sans-serif;
    font-weight: 700;
    font-size: 10px;
    fill: var(--brand-grey);
  }
</style>
</head>
<body>
<main class="template-row">

  <!-- Template A: stadium -->
  <section class="post post--stadium">
    <svg viewBox="0 0 1173 1173" xmlns="http://www.w3.org/2000/svg">
      <defs>
        <linearGradient id="stadium-photo" x1="0" y1="0" x2="0" y2="1">
          <stop offset="0" stop-color="var(--deep-blue)"/>
          <stop offset="0.3" stop-color="var(--sky-blue)"/>
          <stop offset="0.55" stop-color="var(--stadium-blue)"/>
          <stop offset="0.8" stop-color="#16306a"/>
          <stop offset="1" stop-color="var(--pitch-green)"/>
        </linearGradient>
        <linearGradient id="stadium-fade" x1="0" y1="0" x2="0" y2="1">
          <stop offset="0.55" stop-color="#000" stop-opacity="0"/>
          <stop offset="1" stop-color="#000" stop-opacity="0.92"/>
        </linearGradient>
      </defs>
      <rect class="post-photo" role="img" aria-label="Photo: footballer seen from behind holding a ball, facing a floodlit stadium under a stormy sky" width="1173" height="1173" fill="url(#stadium-photo)"/>
      <rect width="1173" height="1173" fill="url(#stadium-fade)"/>

      <g class="accent-shapes">
        <polygon points="0,720 135,628 140,660 0,755" fill="var(--accent-blue)" opacity="0.7"/>
        <polygon points="397,511 505,671 0,1010 0,830" fill="var(--accent-teal)" opacity="0.55"/>
        <polygon points="677,585 865,858 255,883" fill="var(--accent-blue)" opacity="0.6"/>
        <polygon points="0,1035 680,600 685,612 0,1058" fill="#0a1024" opacity="0.75"/>
      </g>

      <text class="headline-lead" x="335" y="820" textLength="585" lengthAdjust="spacingAndGlyphs">THIS IS JUST THE</text>
      <text class="headline-main" x="205" y="963" textLength="733" lengthAdjust="spacingAndGlyphs">BEGINNING</text>

      <g class="brand-lockup">
        <text class="brand-name" x="930" y="1114" textLength="168" lengthAdjust="spacingAndGlyphs">PEAKMIND</text>
        <text class="brand-tagline" x="931" y="1131" textLength="167" lengthAdjust="spacingAndGlyphs">CLEAR FOCUS FOR EVERY MATCH DAY</text>
      </g>
    </svg>
  </section>

  <!-- Template B: strike -->
  <section class="post post--strike">
    <svg viewBox="0 0 1173 1173" xmlns="http://www.w3.org/2000/svg">
      <defs>
        <linearGradient id="strike-photo" x1="0" y1="0" x2="1" y2="1">
          <stop offset="0" stop-color="#15161c"/>
          <stop offset="0.35" stop-color="var(--sock-green)"/>
          <stop offset="0.55" stop-color="var(--boot-lime)"/>
          <stop offset="0.75" stop-color="var(--mist-teal)"/>
          <stop offset="1" stop-color="#1c2a22"/>
        </linearGradient>
        <linearGradient id="strike-fade" x1="0" y1="0" x2="0" y2="1">
          <stop offset="0.5" stop-color="#000" stop-opacity="0"/>
          <stop offset="1" stop-color="#000" stop-opacity="0.92"/>
        </linearGradient>
      </defs>
      <rect class="post-photo" role="img" aria-label="Photo: close-up of a player's boot and green sock striking towards a ball on a misty floodlit pitch" width="1173" height="1173" fill="url(#strike-photo)"/>
      <rect width="1173" height="1173" fill="url(#strike-fade)"/>

      <g class="accent-shapes">
        <polygon points="1173,0 1173,28 930,175 900,160 1110,0" fill="#1a1a22" opacity="0.85"/>
        <polygon points="1173,40 1173,330 450,760 450,470" fill="#5fd0e0" opacity="0.28"/>
        <polygon points="1173,350 1173,368 560,705 555,690" fill="var(--stripe-sand)" opacity="0.8"/>
      </g>

      <text class="headline-lead" x="345" y="838" textLength="585" lengthAdjust="spacingAndGlyphs">THIS IS JUST THE</text>
      <text class="headline-main" x="206" y="975" textLength="732" lengthAdjust="spacingAndGlyphs">BEGINNING</text>

      <g class="brand-lockup">
        <text class="brand-name" x="930" y="1114" textLength="168" lengthAdjust="spacingAndGlyphs">PEAKMIND</text>
        <text class="brand-tagline" x="931" y="1131" textLength="167" lengthAdjust="spacingAndGlyphs">CLEAR FOCUS FOR EVERY MATCH DAY</text>
      </g>
    </svg>
  </section>

</main>
</body>
</html>
```